Rosalind Vetteray Gymnastics Center Business Card

Develop a business card with my RV logo provided. A classy and unique design using the colors black, white, purple and maybe a splash of gold. Add Address (219 W. Lantern Ridge Road Medina, Ohio 44871), email (RosalindVetterayGymnasticsCtr@brellomail.com, website (www.RosalindVetterayGymnasticsCenter.example), phone number (216-555-0148) on the card. Social media if there's room also. t: @VetterayGym, i: @VetterayGym, f: @RosalindVetterayGymnasticsCenter

Target Market(s)

Families, children, gymnastics community and beyond

Industry/Entity Type

Business

Contact Information for Business Card

Add name (Rosalind Vetteray) who is the owner. Add logo, add address details, classy font, uniqueness important, rounded edges on business card. Horizontal business card needed.

Font styles to use
Serif
Sans Serif

Colors
6b449b
ffffff

Requirements
Must have
• Must have logo, owner name and owner on card, must have colors purple, white, black where needed in print, and a splash of gold if appropriate. Keep card classy and clean. Must have address of location, phone number, website of business, email and social media.
Nice to have
• I am open here, but I'd appreciate uniqueness. Must be a lasting image for branding...
Should not have
• No kid-like looks...

```html
<!DOCTYPE html>
<html lang="en">
<head>
<meta charset="utf-8">
<title>Rosalind Vetteray Gymnastics Center – Business Card</title>
<link href="https://fonts.googleapis.com/css2?family=Cinzel:wght@400;600&family=PT+Serif&family=Montserrat:wght@700&display=swap" rel="stylesheet">
<style>
  :root {
    --page: #ece8e6;
    --card: #161616;
    --white: #ffffff;
    --purple: #6b449b;
    --violet: #4b2bd6;
    --gold: #d4b043;
  }
  * { margin: 0; padding: 0; box-sizing: border-box; }
  html, body { width: 1200px; height: 1197px; overflow: hidden; background: var(--page); }
  .sheet { position: relative; width: 1200px; height: 1197px; }
  .card {
    position: absolute; left: 150px; width: 900px; height: 514px;
    background: var(--card); border-radius: 40px; overflow: hidden;
  }
  .card--front { top: 56px; }
  .card--back { top: 627px; }

  /* front */
  .brand { position: absolute; left: 52px; top: 250px; width: 300px; }
  .brand__mark { display: block; width: 34px; height: 34px; background: var(--purple); margin-bottom: 14px; }
  .brand__name {
    font-family: "Montserrat", sans-serif; font-weight: 700; font-size: 21px;
    line-height: 1.15; color: var(--white); text-transform: uppercase; letter-spacing: .5px;
  }
  .brand__tagline {
    margin-top: 8px; font-family: "PT Serif", serif; font-size: 14px; color: var(--violet);
  }
  .divider { position: absolute; left: 372px; top: 190px; width: 3px; height: 290px; background: var(--white); }
  .owner { position: absolute; right: 44px; top: 50px; text-align: right; color: var(--white); }
  .owner__name { font-family: "Cinzel", serif; font-weight: 600; font-size: 46px; letter-spacing: 1px; line-height: 1; }
  .owner__role { font-family: "PT Serif", serif; font-size: 16px; letter-spacing: .5px; margin-top: 6px; text-transform: uppercase; }
  .contacts { position: absolute; left: 398px; top: 160px; list-style: none; }
  .contact {
    display: flex; align-items: center; height: 42px;
    font-family: "PT Serif", serif; font-size: 19px; color: var(--white); white-space: nowrap;
  }
  .contact__icon { width: 24px; height: 24px; margin-right: 16px; flex: none; }

  /* back */
  .back-brand {
    position: absolute; inset: 0; display: flex; align-items: center; justify-content: center; gap: 22px;
  }
  .back-brand__mark { width: 44px; height: 44px; border-radius: 50%; background: var(--gold); }
  .back-brand__name {
    font-family: "Montserrat", sans-serif; font-weight: 700; font-size: 34px; line-height: 1.15;
    color: var(--gold); text-transform: uppercase;
  }
</style>
</head>
<body>
<main class="sheet">
  <section class="card card--front" aria-label="Business card front">
    <header class="owner">
      <h1 class="owner__name">Rosalind Vetteray</h1>
      <p class="owner__role">Personal Coach</p>
    </header>

    <div class="brand">
      <span class="brand__mark"></span>
      <p class="brand__name">Rosalind Vetteray<br>Gymnastics Center</p>
      <p class="brand__tagline">Gymnastics, Cheer, Yoga &amp; More</p>
    </div>

    <span class="divider"></span>

    <ul class="contacts">
      <li class="contact">
        <svg class="contact__icon" viewBox="0 0 24 24"><path d="M6.6 2.5l3 3.2-1.8 2.6c1.2 2.6 3.3 4.7 5.9 5.9l2.6-1.8 3.2 3-1.9 3.3c-7.3-.5-13.3-6.5-13.8-13.8z" fill="#fff"/></svg>
        216-555-0148
      </li>
      <li class="contact">
        <svg class="contact__icon" viewBox="0 0 24 24"><path d="M12 2a7 7 0 0 0-7 7c0 5 7 13 7 13s7-8 7-13a7 7 0 0 0-7-7z" fill="none" stroke="#fff" stroke-width="2"/><circle cx="12" cy="9" r="2.6" fill="#fff"/></svg>
        219 W. Lantern Ridge Road Medina, Ohio 44871
      </li>
      <li class="contact">
        <svg class="contact__icon" viewBox="0 0 24 24"><rect x="2" y="5" width="20" height="14" rx="1" fill="none" stroke="#fff" stroke-width="2"/><path d="M2 6l10 7 10-7" fill="none" stroke="#fff" stroke-width="2"/></svg>
        RosalindVetterayGymnasticsCtr@brellomail.com
      </li>
      <li class="contact">
        <svg class="contact__icon" viewBox="0 0 24 24"><circle cx="12" cy="12" r="6" fill="#fff"/></svg>
        @RosalindVetterayGymnasticsCenter
      </li>
      <li class="contact">
        <svg class="contact__icon" viewBox="0 0 24 24"><circle cx="12" cy="12" r="6" fill="#fff"/></svg>
        @VetterayGym
      </li>
      <li class="contact">
        <svg class="contact__icon" viewBox="0 0 24 24"><circle cx="12" cy="12" r="6" fill="#fff"/></svg>
        @VetterayGym
      </li>
      <li class="contact">
        <svg class="contact__icon" viewBox="0 0 24 24"><g fill="none" stroke="#fff" stroke-width="1.8"><circle cx="12" cy="12" r="9.5"/><ellipse cx="12" cy="12" rx="4.2" ry="9.5"/><path d="M2.5 12h19M4 7h16M4 17h16"/></g></svg>
        www.RosalindVetterayGymnasticsCenter.example
      </li>
    </ul>
  </section>

  <section class="card card--back" aria-label="Business card back">
    <div class="back-brand">
      <span class="back-brand__mark"></span>
      <p class="back-brand__name">Rosalind Vetteray<br>Gymnastics Center</p>
    </div>
  </section>
</main>
</body>
</html>
```